Real Estate Team Business Card

We need a business card designed for our real estate team called "Larkspur Realty Group". We would like to receive a final format that would allow us to edit the contact information for new employees as they are added to our team. The difficult part of the design is that we will need to have two logos on the card - both our team name logo for "Larkspur Realty Group" and our company logo for "Corvane Real Estate". Most emphasis should be given to the team logo - maybe double the size of our company logo. (we just have to have the company logo somewhere on the card for legal purposes) The design should somehow illustrate we work in real estate, but still use the beehive/bee concept as a lot of our marketing will involve "bee" sayings. We would also like to use the tagline: "find out what all the buzz is about". We also need to use the "fair housing" logo and "realtor" logos. These can both be small like the company logo.
Target Market(s)
Real Estate
Industry/Entity Type
Real Estate Agent
Contact Information for Business Card
Name: Dylan Marsh Title: Realtor Phone: 801-555-0172 Email: dylan@larkspurrealtrygroup.com Website: www.larkspurrealtygroup.com Facebook: fb/me/larkspurrealtygroup Twitter: @LarkspurRltyGrp
Colors
Designer to choose colors to be used in the design.
Requirements
Must have
- Contact information. Larkspur Realty Group Logo. Corvane Real Estate Logo. Realtor logo. Fair Housing Logo. Tagline: "find out what all the buzz is about".
Nice to have
- It would be nice to illustrate that we work in real estate. It would also be nice to somehow incorporate bees or play off of our beehive logo. We will do a lot of marking using sayings like "let us bee the solution" or "real estate meant to bee" etc.

```html
<!DOCTYPE html>
<html lang="en">
<head>
<meta charset="utf-8">
<title>Larkspur Realty Group – Business Card</title>
<link rel="stylesheet" href="https://fonts.googleapis.com/css2?family=Quicksand:wght@500;600;700&display=swap">
<style>
  :root {
    --honey: #f6d21b;
    --ink: #1a1a1a;
    --charcoal: #1e1e1e;
    --paper: #ffffff;
    --backdrop: #e9e6df;
    --rule: #5a4a1a;
  }
  * { box-sizing: border-box; margin: 0; padding: 0; }
  html, body { width: 1200px; height: 900px; overflow: hidden; }
  body {
    background: var(--backdrop);
    font-family: "Quicksand", sans-serif;
    color: var(--ink);
    position: relative;
  }
  .card {
    position: absolute;
    left: 285px;
    width: 630px;
    height: 360px;
    background: var(--paper);
    box-shadow: 0 6px 18px rgba(0,0,0,.18);
    overflow: hidden;
  }
  /* Front */
  .card--front { top: 70px; }
  .front__band {
    position: absolute; left: 0; right: 0;
    background: var(--honey);
  }
  .front__band--top {
    top: 0; height: 78px;
    border-bottom: 1.5px solid var(--ink);
    display: flex; align-items: center; justify-content: space-between;
    padding: 0 36px;
  }
  .front__band--bottom {
    bottom: 0; height: 82px;
    border-top: 1.5px solid var(--ink);
    display: flex; align-items: center; justify-content: center;
  }
  .partner-badge {
    width: 30px; height: 30px;
  }
  .partner-badge--solid { background: var(--ink); }
  .partner-badge--outline { border-radius: 4px; border: 3px solid var(--ink); }
  .company-name {
    font-weight: 600; font-size: 22px; color: var(--ink);
    letter-spacing: .5px;
  }
  .tagline {
    font-size: 22px; font-weight: 600; letter-spacing: .3px;
  }
  .team-logo {
    position: absolute;
    display: flex; flex-direction: column; align-items: center;
    font-weight: 600; color: var(--ink);
  }
  .team-logo__mark {
    width: 44px; height: 44px; border-radius: 50%;
    background: var(--honey);
    margin-bottom: 10px;
  }
  .team-logo__name { line-height: 1; letter-spacing: 4px; text-transform: uppercase; }
  .team-logo__sub { line-height: 1; letter-spacing: 4px; text-transform: uppercase; margin-top: 8px; }
  .card--front .team-logo { left: 0; right: 0; top: 98px; }
  .card--front .team-logo__name { font-size: 38px; }
  .card--front .team-logo__sub { font-size: 13px; }

  /* Back */
  .card--back { top: 470px; display: flex; }
  .back__brand {
    width: 250px; height: 100%;
    background: var(--paper);
    border-right: 3px solid var(--honey);
    position: relative;
  }
  .card--back .team-logo { left: 0; right: 0; top: 100px; }
  .card--back .team-logo__mark { width: 56px; height: 56px; margin-bottom: 14px; }
  .card--back .team-logo__name { font-size: 30px; letter-spacing: 3px; }
  .card--back .team-logo__sub { font-size: 12px; letter-spacing: 3px; }
  .back__details {
    flex: 1; background: var(--charcoal);
    padding: 52px 36px 0 36px;
    color: var(--honey);
  }
  .agent-name {
    font-size: 25px; font-weight: 500;
    padding-bottom: 8px;
    border-bottom: 1px solid var(--rule);
    width: 300px;
  }
  .contact-list { list-style: none; margin-top: 18px; }
  .contact-list li {
    display: flex; align-items: center; gap: 14px;
    font-size: 16px; font-weight: 500; height: 31px;
    white-space: nowrap;
  }
  .contact-icon { width: 20px; height: 20px; flex: none; }
</style>
</head>
<body>

<section class="card card--front">
  <div class="front__band front__band--top">
    <span class="partner-badge partner-badge--solid" role="img" aria-label="Membership badge"></span>
    <span class="company-name">Corvane Real Estate</span>
    <span class="partner-badge partner-badge--outline" role="img" aria-label="Housing policy badge"></span>
  </div>
  <div class="team-logo">
    <span class="team-logo__mark"></span>
    <span class="team-logo__name">Larkspur</span>
    <span class="team-logo__sub">Realty Group</span>
  </div>
  <div class="front__band front__band--bottom">
    <p class="tagline">find out what all the buzz is about</p>
  </div>
</section>

<section class="card card--back">
  <div class="back__brand">
    <div class="team-logo">
      <span class="team-logo__mark"></span>
      <span class="team-logo__name">Larkspur</span>
      <span class="team-logo__sub">Realty Group</span>
    </div>
  </div>
  <div class="back__details">
    <h1 class="agent-name">Dylan Marsh</h1>
    <ul class="contact-list">
      <li>
        <svg class="contact-icon" viewBox="0 0 20 20" fill="none" stroke="#f6d21b" stroke-width="1.2"><circle cx="10" cy="10" r="9"/><path d="M7 6l1.5-.5 1 2-1 1a5 5 0 0 0 2.5 2.5l1-1 2 1-.5 1.5c-3 .5-7-3.5-6.5-6.5z" fill="#f6d21b" stroke="none"/></svg>
        <span>801-555-0172</span>
      </li>
      <li>
        <svg class="contact-icon" viewBox="0 0 20 20" fill="none" stroke="#f6d21b" stroke-width="1.2"><circle cx="10" cy="10" r="9"/><rect x="5.5" y="7" width="9" height="6.5"/><path d="M5.5 7l4.5 3.5L14.5 7"/></svg>
        <span>dylan@larkspurrealtrygroup.com</span>
      </li>
      <li>
        <svg class="contact-icon" viewBox="0 0 20 20" fill="none" stroke="#f6d21b" stroke-width="1.2"><circle cx="10" cy="10" r="9"/><circle cx="10" cy="10" r="5"/><ellipse cx="10" cy="10" rx="2.2" ry="5"/><path d="M5 10h10"/></svg>
        <span>www.larkspurrealtygroup.com</span>
      </li>
      <li>
        <svg class="contact-icon" viewBox="0 0 20 20" fill="none" stroke="#f6d21b" stroke-width="1.2"><circle cx="10" cy="10" r="9"/></svg>
        <span>fb/me/larkspurrealtygroup</span>
      </li>
      <li>
        <svg class="contact-icon" viewBox="0 0 20 20" fill="none" stroke="#f6d21b" stroke-width="1.2"><circle cx="10" cy="10" r="9"/></svg>
        <span>@LarkspurRltyGrp</span>
      </li>
    </ul>
  </div>
</section>

</body>
</html>
```